Contemporary new French wine brand needs logo and series of label design

to design a new contemporary logo and series of labels for a new French wine brand. We hope to attract not just current French wine drinkers but new ones who may appreciate a less traditional and more modern style.

Reason: we are wanting to extend the project for a few days more to receive more submissions since we had fewer designs submitted than we were expecting, maybe because of the holidays.

Target Market(s)

people who follow the arts community (eg. music, theatre, visual/video arts, dance) --- all mature ages.

Industry/Entity Type

French Wine

Requirements
Must have
• a clear, memorable treatment for the name BRUMAIS with accompanying logo.
Nice to have
• embossing, matte/gloss refinement, tasteful foil stamping, coated stock for the whites to help the integrity of the paper in and out of ice buckets. A combo of say, three types of fonts; a semi custom font for the brand name Brumais and maybe a script and one other.
Should not have
• not traditional French

```html
<!DOCTYPE html>
<html lang="fr">
<head>
<meta charset="utf-8">
<title>Brumais — Label Series</title>
<link rel="stylesheet" href="https://fonts.googleapis.com/css2?family=Cinzel:wght@500&family=Pinyon+Script&family=Cormorant+Garamond:wght@500&display=swap">
<style>
  :root {
    --backdrop: #6e6e6e;
    --red-stock: #2a2d2c;
    --red-stock-edge: #1f2221;
    --red-ink: #c9c9c9;
    --red-rule: #8a8c8b;
    --white-stock-a: #f4f4f4;
    --white-stock-b: #cfd0d0;
    --white-ink: #1c1c1c;
    --white-rule: #4d4d4d;
    --region-red: #b3203b;
  }
  * { box-sizing: border-box; margin: 0; padding: 0; }
  html, body { width: 1200px; height: 970px; overflow: hidden; }
  body {
    background: var(--backdrop);
    display: flex;
    align-items: center;
    justify-content: center;
    gap: 34px;
  }
  .label {
    width: 256px;
    height: 324px;
    padding: 7px;
    box-shadow: 0 4px 14px rgba(0,0,0,.28);
  }
  .label--red {
    background: radial-gradient(ellipse at 50% 35%, var(--red-stock), var(--red-stock-edge));
    color: var(--red-ink);
    --rule: var(--red-rule);
  }
  .label--white {
    background: linear-gradient(160deg, var(--white-stock-a) 0%, #e2e3e3 45%, var(--white-stock-b) 100%);
    color: var(--white-ink);
    --rule: var(--white-rule);
  }
  .label__frame {
    height: 100%;
    border: 1px solid var(--rule);
    outline: 1px solid var(--rule);
    outline-offset: 3px;
    display: flex;
    flex-direction: column;
    align-items: center;
    padding-top: 24px;
  }
  .brand-dot {
    width: 32px;
    height: 32px;
    border-radius: 50%;
    border: 1.5px solid currentColor;
  }
  .brand-name {
    font-family: "Cinzel", serif;
    font-weight: 500;
    font-size: 26px;
    letter-spacing: 3px;
    margin-top: 8px;
    line-height: 1;
  }
  .artwork {
    margin-top: 22px;
    height: 56px;
  }
  .artwork--landscape-abstract { width: 108px; }
  .artwork--estate { width: 160px; height: 66px; margin-top: 16px; }
  .label--red .artwork--landscape-abstract { background: linear-gradient(170deg, #000 0%, #3a3a3a 45%, #0a0a0a 70%, #555 100%); }
  .label--red .artwork--estate { background: linear-gradient(180deg, rgba(190,190,190,.15) 0%, rgba(170,170,170,.55) 55%, rgba(120,120,120,.35) 100%); }
  .label--white .artwork--landscape-abstract { background: linear-gradient(170deg, #f2f2f2 0%, #9a9a9a 45%, #e6e6e6 70%, #7a7a7a 100%); }
  .label--white .artwork--estate { background: linear-gradient(180deg, rgba(60,60,60,.12) 0%, rgba(30,30,30,.6) 55%, rgba(60,60,60,.35) 100%); }
  .varietal {
    font-family: "Pinyon Script", cursive;
    font-size: 27px;
    margin-top: 14px;
    line-height: 1.1;
  }
  .artwork--estate + .varietal { margin-top: 4px; }
  .vintage {
    display: flex;
    align-items: center;
    gap: 8px;
    font-family: "Cormorant Garamond", serif;
    font-weight: 500;
    font-size: 13px;
    letter-spacing: 1.5px;
    margin-top: 12px;
  }
  .vintage::before, .vintage::after {
    content: "";
    width: 46px;
    height: 1px;
    background: currentColor;
  }
  .region {
    font-family: "Cormorant Garamond", serif;
    font-weight: 500;
    font-size: 12px;
    letter-spacing: 1px;
    color: var(--region-red);
    margin-top: 18px;
  }
  .label--red .region { opacity: .75; }
</style>
</head>
<body>
  <article class="label label--red">
    <div class="label__frame">
      <span class="brand-dot"></span>
      <h1 class="brand-name">BRUMAIS</h1>
      <div class="artwork artwork--landscape-abstract" role="img" aria-label="Abstract flowing landscape lines in black and grey"></div>
      <p class="varietal">Cabernet Franc</p>
      <p class="vintage">2014</p>
      <p class="region">Val de Loire</p>
    </div>
  </article>

  <article class="label label--red">
    <div class="label__frame">
      <span class="brand-dot"></span>
      <h1 class="brand-name">BRUMAIS</h1>
      <div class="artwork artwork--estate" role="img" aria-label="Engraved drawing of a château among vineyard rows"></div>
      <p class="varietal">Cabernet Franc</p>
      <p class="vintage">2014</p>
      <p class="region">Val de Loire</p>
    </div>
  </article>

  <article class="label label--white">
    <div class="label__frame">
      <span class="brand-dot"></span>
      <h1 class="brand-name">BRUMAIS</h1>
      <div class="artwork artwork--landscape-abstract" role="img" aria-label="Abstract flowing landscape lines in silver tones"></div>
      <p class="varietal">Sauvignon Blanc</p>
      <p class="vintage">2014</p>
      <p class="region">Val de Loire</p>
    </div>
  </article>

  <article class="label label--white">
    <div class="label__frame">
      <span class="brand-dot"></span>
      <h1 class="brand-name">BRUMAIS</h1>
      <div class="artwork artwork--estate" role="img" aria-label="Engraved drawing of a château among vineyard rows"></div>
      <p class="varietal">Sauvignon Blanc</p>
      <p class="vintage">2014</p>
      <p class="region">Val de Loire</p>
    </div>
  </article>
</body>
</html>
```